5 facebook (and instagram) posts for advertising a service of Online Medicine.
This is NOT a facebook page design. This is just facebook (and Instagram) posts design.

We are a medical company providing medicine at distance, using standard videoconsultation and sometimes videoconsultation with a medical device that collects vital signs.

Each post should have:
- Our logo (attached) – if needed it can be just the circular form, but that´s up to you to decide. Ofcourse some design work can be done to this form (watermark, change in dimension, etc)
- Some posts can have the photo of the device (not all the posts because we also provide videoconsultations without the device) – for this please use our website to collect images (https://www.casaorvalhoverde.com/en/kordalix). You can also use the video of the device to collect images (provided as attachment).
- Some stock image at your decision or collected from our website (https://www.casaorvalhoverde.com/pt/medicina-online) or from the provided video (all of these are licensed and you can use them freely – for instance you can collect doctors from our video)
- One or more of the following headlines (please use different headlines for different posts):
 Revolução na Qualidade da Videoconsulta
 O seu Médico com acesso à informação da sua Orrin Wellbook
 Sincronização com Orrin Wellbook
 Possibilidade de usar o dispositivo Kordalix | Medição à Distância de 6 Sinais Vitais
 Revolução na Saúde
 Revolução na Medicina à Distância
 Um Novo Mundo na Saúde
 Segurança e Fiabilidade na Medicina à Distância
 Excelência na Medicina à Distância
 Baixa Médica Online
 Atestados de Saúde
 Renovação de Receituário
 Planos de Monitorização Remota e Acompanhamento Médico desde 10 EUR / Mês

We need 5 posts, all different between each other but where we can feel an aesthetical and graphic/design continuity/coherence of course.
Each post should be provided on adequate format for facebook and Instagram publishing.

Target Market(s)

Patients

Industry/Entity Type

Medicine

Requirements
Must have
• Check description
Nice to have
• Check description

```html
<!DOCTYPE html>
<html lang="pt">
<head>
<meta charset="utf-8">
<title>Casa Orvalho Verde — Planos de Monitorização Remota</title>
<link rel="stylesheet" href="https://fonts.googleapis.com/css2?family=Oswald:wght@500;600&family=Open+Sans:wght@400;600;700;800&display=swap">
<style>
  :root {
    --brand-blue: #1e9bd4;
    --brand-blue-deep: #1582b8;
    --brand-blue-soft: #5cc0e6;
    --accent-orange: #e8832a;
    --ink: #1c1c1c;
    --ink-muted: #6b6b6b;
    --paper: #f3f4f6;
    --white: #ffffff;
  }
  * { margin: 0; padding: 0; box-sizing: border-box; }
  html, body { width: 1200px; height: 1200px; overflow: hidden; background: var(--paper); }
  .post {
    position: relative; width: 1200px; height: 1200px; overflow: hidden;
    background: linear-gradient(135deg, #ffffff 0%, #eef0f3 45%, #f7f8fa 70%, #e9ebee 100%);
    font-family: "Open Sans", sans-serif;
  }
  .backdrop { position: absolute; inset: 0; }
  .brand-card {
    position: absolute; left: 72px; top: 0; width: 367px; height: 144px;
    background: var(--white); border-radius: 0 0 24px 24px;
    display: flex; align-items: center; padding-left: 38px; gap: 14px;
  }
  .brand-mark { width: 52px; height: 52px; background: var(--brand-blue); border-radius: 8px; flex: none; }
  .brand-name {
    font-family: "Oswald", sans-serif; font-weight: 600; color: var(--brand-blue);
    font-size: 30px; line-height: 1; text-transform: uppercase; letter-spacing: 0.5px;
  }
  .brand-tagline { margin-top: 6px; font-size: 13px; color: var(--ink-muted); }
  .hero-ring {
    position: absolute; left: 233px; top: 131px; width: 716px; height: 716px;
    border-radius: 50%; background: var(--accent-orange);
  }
  .hero-photo {
    position: absolute; left: 27px; top: 27px; width: 662px; height: 662px; border-radius: 50%;
    background: radial-gradient(circle at 65% 55%, #e6ded4 0%, #b9aea0 40%, #7d6f62 75%, #5d5249 100%);
  }
  .offer-box {
    position: absolute; left: 164px; top: 883px; width: 875px; height: 195px;
    border: 2px solid var(--accent-orange); border-radius: 10px;
    background: rgba(255,255,255,0.6); text-align: center;
  }
  .offer-title {
    margin-top: 32px; font-family: "Oswald", sans-serif; font-weight: 500;
    font-size: 31px; line-height: 39px; color: var(--brand-blue); text-transform: uppercase;
  }
  .offer-price {
    display: inline-block; background: var(--accent-orange); color: var(--white);
    padding: 0 14px; margin-left: 2px; transform: skewX(-6deg);
  }
  .offer-price span { display: inline-block; transform: skewX(6deg); }
  .offer-sub {
    margin-top: 18px; display: flex; align-items: center; justify-content: center; gap: 18px;
    font-weight: 700; font-size: 19px; color: var(--ink); text-transform: uppercase;
  }
  .offer-sub::before, .offer-sub::after {
    content: ""; width: 56px; height: 2px; background: var(--accent-orange);
  }
  .contact-phone { position: absolute; left: 62px; top: 1126px; display: flex; align-items: center; gap: 16px; }
  .icon-badge {
    width: 54px; height: 54px; border-radius: 50%; background: var(--brand-blue);
    display: flex; align-items: center; justify-content: center; flex: none;
  }
  .contact-label { font-size: 13px; color: var(--ink); }
  .contact-number { font-size: 22px; font-weight: 800; color: var(--ink); line-height: 1.2; }
  .cta {
    position: absolute; left: 441px; top: 1129px; width: 278px; height: 51px;
    background: var(--brand-blue); border-radius: 4px; color: var(--white);
    font-weight: 700; font-size: 25px; display: flex; align-items: center; justify-content: center;
  }
  .contact-web { position: absolute; left: 802px; top: 1128px; display: flex; align-items: center; gap: 12px; }
  .contact-url { font-size: 19px; font-weight: 700; color: var(--ink); }
</style>
</head>
<body>
<main class="post">
  <svg class="backdrop" width="1200" height="1200" viewBox="0 0 1200 1200" role="img" aria-label="Faded blue-toned photo of a medical team at work">
    <defs>
      <linearGradient id="teamTint" x1="0" y1="0" x2="1" y2="1">
        <stop offset="0" stop-color="#2aa6dc"/>
        <stop offset="0.5" stop-color="#4db8e4"/>
        <stop offset="1" stop-color="#1e8fc8"/>
      </linearGradient>
    </defs>
    <path d="M0 0 H1200 V660 Q600 300 0 640 Z" fill="url(#teamTint)"/>
  </svg>

  <header class="brand-card">
    <div class="brand-mark"></div>
    <div>
      <div class="brand-name">Casa Orvalho Verde</div>
      <div class="brand-tagline">Professor Doutor Rui Tavares Lemos</div>
    </div>
  </header>

  <div class="hero-ring">
    <div class="hero-photo" role="img" aria-label="Woman on a sofa with a blood pressure cuff on her arm, talking to a doctor by video call on her laptop"></div>
  </div>

  <section class="offer-box">
    <h1 class="offer-title">Planos de Monitorização<br>Remota e Acompanhamento Médico desde<span class="offer-price"><span>10 EUR / Mês</span></span></h1>
    <p class="offer-sub">Cuide da sua saúde sem sair de casa!</p>
  </section>

  <div class="contact-phone">
    <div class="icon-badge">
      <svg width="26" height="26" viewBox="0 0 24 24" aria-hidden="true"><path fill="#fff" d="M6.6 10.8a15.1 15.1 0 0 0 6.6 6.6l2.2-2.2c.3-.3.7-.4 1-.2 1.1.4 2.3.6 3.6.6.6 0 1 .4 1 1V20c0 .6-.4 1-1 1A17 17 0 0 1 3 4c0-.6.4-1 1-1h3.5c.6 0 1 .4 1 1 0 1.3.2 2.5.6 3.6.1.3 0 .7-.2 1z"/></svg>
    </div>
    <div>
      <div class="contact-label">Ligue-nos para mais informações</div>
      <div class="contact-number">+351 912 480 375</div>
    </div>
  </div>

  <div class="cta">Consulte Agora</div>

  <div class="contact-web">
    <div class="icon-badge">
      <svg width="28" height="28" viewBox="0 0 24 24" aria-hidden="true" fill="none" stroke="#fff" stroke-width="1.6"><circle cx="12" cy="12" r="9"/><ellipse cx="12" cy="12" rx="4" ry="9"/><path d="M3 12h18M4.5 7.5h15M4.5 16.5h15"/></svg>
    </div>
    <div class="contact-url">www.casaorvalhoverde.com</div>
  </div>
</main>
</body>
</html>
```